IG ad to attract older men for better health #1

I want a bold headline Instagram Ad that coordinate with my website design with a racy sexy woman to attract men 45yrs old plus. See Two samples attached

Target Market(s)

Men 45 years old and older

Industry/Entity Type

Health And Wellness

Requirements
Must have
• eye catching appeal to men
Nice to have
• The copy to read
Kestrel61go is the headline at the top of the page. Then the copy reads...
"I want to seduce you to better health with a little T&A. Remove the excuses, provide ridiculously simple tips and advice to get you started on a path of lasting heath." Want more?

```html
<!DOCTYPE html>
<html lang="en">
<head>
<meta charset="UTF-8">
<title>Kestrel61go – Better Health Ad</title>
<link href="https://fonts.googleapis.com/css2?family=Oswald:wght@500;600;700&display=swap" rel="stylesheet">
<style>
  :root {
    --red: #c8102e;
    --yellow: #f6e600;
    --ink: #1c1c1c;
    --paper: #f7f5f3;
    --photo-light: #ece6e2;
    --photo-mid: #d9c9bf;
    --photo-skin: #d9a483;
  }
  * { margin: 0; padding: 0; box-sizing: border-box; }
  html, body { width: 1200px; height: 1200px; overflow: hidden; }
  body { font-family: "Oswald", "Arial Narrow", sans-serif; background: var(--paper); }

  .ad {
    position: relative;
    width: 1200px;
    height: 1200px;
    overflow: hidden;
    background: linear-gradient(100deg, var(--paper) 0%, var(--photo-light) 55%, var(--photo-mid) 100%);
  }

  .model-photo {
    position: absolute;
    left: 700px;
    top: 60px;
    width: 460px;
    height: 1140px;
    border-radius: 200px 200px 0 0;
    background: linear-gradient(180deg, #e8cf98 0%, var(--photo-skin) 30%, var(--red) 55%, var(--photo-skin) 85%, #cfa285 100%);
    opacity: 0.85;
  }

  .brand-pill {
    position: absolute;
    left: 152px;
    top: 97px;
    width: 431px;
    height: 109px;
    border-radius: 55px;
    background: var(--red);
    display: flex;
    align-items: center;
    justify-content: center;
    color: var(--yellow);
    font-weight: 700;
    font-size: 72px;
    letter-spacing: 1px;
    text-transform: uppercase;
  }

  .quote-mark {
    position: absolute;
    color: var(--red);
    font-weight: 700;
    font-size: 110px;
    line-height: 1;
  }
  .quote-open { left: 52px; top: 225px; }
  .quote-close { left: 585px; top: 960px; }

  .copy {
    position: absolute;
    left: 57px;
    width: 620px;
    text-align: center;
    color: var(--ink);
    text-transform: uppercase;
    font-weight: 600;
  }
  .lead { top: 305px; font-size: 46px; line-height: 1; }
  .headline { top: 385px; font-size: 80px; line-height: 1; font-weight: 700; }
  .headline .accent { color: var(--red); }
  .subline { top: 480px; font-size: 52px; line-height: 1; }
  .body-text { top: 588px; font-size: 47px; line-height: 61px; }
  .cta { top: 1030px; font-size: 68px; line-height: 1; font-weight: 700; color: var(--red); }
</style>
</head>
<body>
  <main class="ad">
    <div class="model-photo" role="img" aria-label="Photo of a blonde woman in a red high-cut swimsuit, seen from behind, turning her head to the side"></div>

    <div class="brand-pill">Kestrel61go</div>

    <span class="quote-mark quote-open">"</span>
    <p class="copy lead">I want to seduce you to</p>
    <p class="copy headline">Better <span class="accent">Health</span></p>
    <p class="copy subline">With a little T&amp;A.</p>
    <p class="copy body-text">Remove the excuses,<br>provide ridiculously simple<br>tips and advice to get you<br>started on a path<br>of lasting heath.</p>
    <p class="copy cta">Want more?</p>
    <span class="quote-mark quote-close">"</span>
  </main>
</body>
</html>
```